Business Card for Brevel Coatings

We need a simple, yet out standing business card for our painting company.

Target Market(s)

wealthy; high-end neighborhoods, and businesses

Industry/Entity Type

Painting

Contact Information for Business Card

Name:
Doran Vask

Email:
d.vask@brevel-coatings.com

Website:
Brevel-coatings.com

Phone Number:
(555) 416-9073

Font styles to use
Serif
Sans Serif

Requirements
Must have
• slogan "making change simple"
Should not have
• A title attached to the name on the card

```html
<!DOCTYPE html>
<html lang="en">
<head>
<meta charset="utf-8">
<title>Brevel Coatings – Business Card</title>
<link rel="stylesheet" href="https://fonts.googleapis.com/css2?family=Cormorant+Garamond:wght@600&family=Roboto:wght@400;700&display=swap">
<style>
  :root {
    --page-bg: #ffffff;
    --card-bg: #ffffff;
    --card-border: #231f20;
    --text-grey: #6d6e71;
    --accent-lime: #a9c23c;
    --brand-green: #3f5a23;
  }
  html, body {
    margin: 0;
    padding: 0;
    width: 1200px;
    height: 1100px;
    overflow: hidden;
    background: var(--page-bg);
  }
  .canvas {
    position: relative;
    width: 1200px;
    height: 1100px;
  }
  .card {
    position: absolute;
    left: 72px;
    top: 222px;
    width: 1048px;
    height: 597px;
    border: 4px solid var(--card-border);
    background: var(--card-bg);
    font-family: "Roboto", Arial, sans-serif;
    color: var(--text-grey);
    text-align: center;
  }
  .holder-name {
    position: absolute;
    left: 0; right: 0;
    top: 62px;
    margin: 0;
    font-size: 48px;
    font-weight: 700;
    line-height: 1.1;
    letter-spacing: 0.5px;
  }
  .holder-email {
    position: absolute;
    left: 0; right: 0;
    top: 118px;
    font-size: 36px;
    line-height: 1.1;
    letter-spacing: 0.5px;
  }
  .holder-email .at { color: var(--accent-lime); }
  .brand {
    position: absolute;
    left: 0; right: 0;
    top: 228px;
    display: flex;
    flex-direction: column;
    align-items: center;
  }
  .brand-line {
    display: flex;
    align-items: center;
    gap: 18px;
  }
  .brand-dot {
    width: 20px;
    height: 20px;
    border-radius: 50%;
    background: var(--brand-green);
  }
  .brand-name {
    font-family: "Cormorant Garamond", Georgia, serif;
    font-size: 66px;
    font-weight: 600;
    line-height: 1;
    color: var(--brand-green);
    letter-spacing: 0.5px;
  }
  .slogan {
    margin-top: 10px;
    font-family: "Cormorant Garamond", Georgia, serif;
    font-size: 27px;
    font-weight: 600;
    line-height: 1;
    color: var(--accent-lime);
    text-transform: uppercase;
    letter-spacing: 8px;
  }
  .holder-phone {
    position: absolute;
    left: 0; right: 0;
    top: 418px;
    font-size: 46px;
    line-height: 1.1;
    letter-spacing: 1px;
  }
  .holder-phone .label {
    color: var(--accent-lime);
    font-weight: 700;
    font-size: 36px;
    margin-right: 12px;
  }
  .website {
    position: absolute;
    left: 0; right: 0;
    top: 518px;
    font-size: 36px;
    line-height: 1.1;
    letter-spacing: 0.5px;
  }
  .website strong { font-weight: 700; }
</style>
</head>
<body>
<div class="canvas">
  <section class="card">
    <h1 class="holder-name">Doran Vask</h1>
    <div class="holder-email">d.vask<span class="at">@</span>brevel-coatings.com</div>
    <div class="brand">
      <div class="brand-line">
        <span class="brand-dot"></span>
        <span class="brand-name">Brevel Coatings</span>
      </div>
      <div class="slogan">making change simple</div>
    </div>
    <div class="holder-phone"><span class="label">T:</span>(555) 416-9073</div>
    <div class="website"><strong>Brevel</strong>-coatings.com</div>
  </section>
</div>
</body>
</html>
```